Animated Graphics for Article-Author Connection App

An Zoka for editor and writers. We want to show screens for a app that connects editor that need articles written and authors who want to write them. But a car/map analogy doesn't work. How about a sun and planet analogy. This can be done withe the following screens:

Screen 1. icons of various industries (aviation, architecture, manufacturing, etc.)

Screen 2. one industry (aviation, shown with a plane icon) shoots out an idea (use light bulb icon) to writers, who appear in an arc around the airplane. Like planets in stationary orbit. When the idea nears the arc, the writer rotates in the orbit to accept it and glows.
Screen 3. writer shoots out article to tech editor
Screen 4. tech editor shoots out article to copy editors
Screen 5. copy editor shoots out article to production person

Target Market(s)

Engineers, editors, authors

Industry/Entity Type

Mechanical Engineering

Colors
dbdbdb
aaaaaa
000000
33a6d7
85acd3
3276b5

Requirements
Must have
• Simple and attractive. Color scheme like Zoka.
Nice to have
• The article or idea have a flag on which 3 pieces of information are shown
• 1) due date
• 2) length
• 3)price

```html
<!DOCTYPE html>
<html lang="en">
<head>
<meta charset="utf-8">
<title>Article Flow — Copy Editor to Production</title>
<link rel="stylesheet" href="https://fonts.googleapis.com/css2?family=Roboto+Condensed:wght@400&display=swap">
<style>
  :root {
    --bg-center: #ffffff;
    --bg-edge: #dbdbdb;
    --ink: #000000;
    --arrow: #1a1a1a;
    --person-light: #85acd3;
    --person-main: #33a6d7;
    --person-deep: #3276b5;
    --outline: #000000;
    --doc-paper: #ffffff;
    --doc-line: #3276b5;
  }
  html, body {
    margin: 0;
    padding: 0;
    overflow: hidden;
  }
  .canvas {
    position: relative;
    width: 849px;
    height: 1200px;
    overflow: hidden;
    background: radial-gradient(ellipse at 45% 45%, var(--bg-center) 0%, #f2f2f2 45%, var(--bg-edge) 100%);
    font-family: "Roboto Condensed", "Arial Narrow", sans-serif;
  }
  .flow-arrows {
    position: absolute;
    inset: 0;
    width: 849px;
    height: 1200px;
  }
  .flow-arrows path.link {
    fill: none;
    stroke: var(--arrow);
    stroke-width: 3;
    stroke-dasharray: 12 7;
  }
  .role {
    position: absolute;
    width: 200px;
    display: flex;
    flex-direction: column;
    align-items: center;
  }
  .role__icon {
    width: 120px;
    height: 156px;
    display: block;
  }
  .role__label {
    margin: 14px 0 0;
    font-size: 22px;
    line-height: 1;
    color: var(--ink);
    text-transform: uppercase;
    white-space: nowrap;
  }
  .role--copy-editor { left: 104px; top: 384px; }
  .role--production-first { left: 582px; top: 231px; }
  .role--production-second { left: 562px; top: 627px; }
  .role--production-third { left: 378px; top: 924px; }
  .article-doc {
    position: absolute;
    left: 462px;
    top: 508px;
    width: 96px;
    height: 118px;
  }
</style>
</head>
<body>
<main class="canvas">
  <svg width="0" height="0" style="position:absolute" aria-hidden="true">
    <defs>
      <linearGradient id="person-fill" x1="0" y1="0" x2="0.4" y2="1">
        <stop offset="0" stop-color="#85acd3"/>
        <stop offset="0.45" stop-color="#33a6d7"/>
        <stop offset="1" stop-color="#3276b5"/>
      </linearGradient>
      <symbol id="user-icon" viewBox="0 0 120 156">
        <path d="M8 150 L8 122 Q8 84 60 84 Q112 84 112 122 L112 150 Q112 153 109 153 L11 153 Q8 153 8 150 Z" fill="url(#person-fill)" stroke="#000" stroke-width="3"/>
        <circle cx="60" cy="42" r="36" fill="url(#person-fill)" stroke="#000" stroke-width="3"/>
        <ellipse cx="48" cy="28" rx="14" ry="9" fill="#ffffff" opacity="0.45"/>
        <path d="M22 110 Q30 94 50 92" fill="none" stroke="#ffffff" stroke-width="5" stroke-linecap="round" opacity="0.45"/>
      </symbol>
    </defs>
  </svg>

  <svg class="flow-arrows" viewBox="0 0 849 1200" aria-hidden="true">
    <defs>
      <marker id="arrow-head" viewBox="0 0 10 10" refX="8" refY="5" markerWidth="5" markerHeight="5" orient="auto">
        <path d="M0 0 L10 5 L0 10 Z" fill="#1a1a1a"/>
      </marker>
    </defs>
    <path class="link" d="M283 498 Q400 476 455 540" marker-end="url(#arrow-head)"/>
    <path class="link" d="M722 462 Q775 540 740 628" marker-end="url(#arrow-head)"/>
    <path class="link" d="M657 852 Q650 965 555 1005" marker-end="url(#arrow-head)"/>
  </svg>

  <section class="role role--copy-editor">
    <svg class="role__icon" role="img" aria-label="Copy editor user icon"><use href="#user-icon"/></svg>
    <p class="role__label">Copy Editor</p>
  </section>

  <svg class="article-doc" viewBox="0 0 96 118" role="img" aria-label="Article document icon">
    <path d="M10 14 L70 14 L86 30 L86 112 L10 112 Z" fill="var(--doc-paper)" stroke="var(--doc-line)" stroke-width="3" stroke-linejoin="round"/>
    <path d="M70 14 L70 30 L86 30" fill="none" stroke="var(--doc-line)" stroke-width="3" stroke-linejoin="round"/>
    <g fill="none" stroke="var(--doc-line)" stroke-width="3" stroke-linecap="round">
      <circle cx="24" cy="10" r="5"/>
      <circle cx="40" cy="10" r="5"/>
      <circle cx="56" cy="10" r="5"/>
      <line x1="22" y1="44" x2="74" y2="44"/>
      <line x1="22" y1="58" x2="74" y2="58"/>
      <line x1="22" y1="72" x2="74" y2="72"/>
      <line x1="22" y1="86" x2="60" y2="86"/>
      <line x1="22" y1="100" x2="52" y2="100"/>
    </g>
  </svg>

  <section class="role role--production-first">
    <svg class="role__icon" role="img" aria-label="Production user icon"><use href="#user-icon"/></svg>
    <p class="role__label">Production</p>
  </section>

  <section class="role role--production-second">
    <svg class="role__icon" role="img" aria-label="Production user icon"><use href="#user-icon"/></svg>
    <p class="role__label">Production</p>
  </section>

  <section class="role role--production-third">
    <svg class="role__icon" role="img" aria-label="Production user icon"><use href="#user-icon"/></svg>
    <p class="role__label">Production</p>
  </section>
</main>
</body>
</html>
```